Web design for our new company

We need a web design for our product and for our company.
And the main is our Product tool called "velmora".
----------------------------------------------------------
[Our company's Goal]
Make organization’s communication smooth and healthy with transparency and efficiency for works and tasks in all levels with our workflow tool.

[Our Mission]
Our mission is to achieve business goals with customers.
We work together to identify the goals for your company, guides your strategy and bring the technology answers which best fit to achieve the goals.

[What we do]
We have a workflow tool "velmora"
- Very simple end-user configurable workflow for any company processes
(Targeting small-med size company)
- Graphical & fun features for startup users
- Simple and easy task control with quillbox e-mail look & feel
- Non charged skill up guidance
- Additional features with;
Multiple delegation
Clear status for each owner
Task owner management console with due date reminders&reporting

Others
1. System Development & Implementation Service
Our client list includes a wide variety of small to medium to major sized enterprises.
We can offer from full-scratch based development to packaged system implementation.

2. Project Management(PM) Service
We will provide end-to-end PM service with experienced PM.
Our service is not only “managing” but “leading” to bring success to achieve the goal.

3.Consultation Service

Consulting services to a wide range of fields such as creating business strategy, business process Kaizen, IT system consultation and change management.

Target Market(s)

Business to Business
Mainly to medium size - startup company

Industry/Entity Type

It Company

Coding

Coded - Design and coding required

Number of Pages Required

5+ page

Colors
0255a3
33a6d7
86cfc6
33b8a4
add136
cadf82
fbf289
fee18a
faa54b

Requirements
Must have
• We need Pages for
• Company mission
• Service Overview
• Contact
• Privacy Policy
• Terms and Conditions
• =========================
• As there were some questions, I add followings.---------
• 1. File Format
• We are going to use Brixel cloud services to upload finished web files.
• The finished files should be ready to use by simply replacing images and text.
• Please provide me "easy to handle" template with "sophisticated design".
• Thanks!
• 2. Multiple Languages
• We need buttons for changing language.
• We will have this translated to German, English and Japanese.
• Thank you so much!!
Nice to have
• These are current Logos and will be a next project to revise them...
• Attached Company Profile and Logo design
• 1. Company Profile
• 2. Our Company Logo
• 3. Our Product Logo -> This is most close to our image of design base.
• 4. Product Logo for PPT Header
• All just for your reference.
• ---------
• As there were some request, I added attachment as for contents for Our mission page.
Should not have
• I hope to see some unique designs.
• (Sorry please ignore my last update as I checked with our CEO.
• Bootstrap is absolutely good template.)

```html
<!DOCTYPE html>
<html lang="en">
<head>
<meta charset="utf-8">
<title>Ternly – IT Consulting and System Development</title>
<link href="https://fonts.googleapis.com/css2?family=Open+Sans:wght@400;600;700&display=swap" rel="stylesheet">
<style>
:root{
  --navy:#0e3d8a;
  --teal:#2aa58f;
  --teal-soft:#76c6b8;
  --brand-green:#7a9a2c;
  --ink:#222;
  --text:#444;
  --muted:#8a93a6;
  --grey-band:#e9ecee;
  --grey-light:#f3f3f3;
  --card-line:#b5bcc1;
  --footer:#141a33;
  --lang:#777;
  --lang-active:#f39a2e;
}
*{box-sizing:border-box;margin:0;padding:0}
html,body{width:1200px;height:2177px;overflow:hidden}
body{position:relative;background:var(--grey-light);font-family:"Open Sans",Arial,sans-serif;color:var(--text)}
.abs{position:absolute}
.page-bg{left:0;top:0;width:1200px;height:2177px}

/* header */
.site-header{left:0;top:0;width:1200px;height:133px;background:#fff}
.brand{left:130px;top:46px;display:flex;align-items:center;gap:10px;font-size:30px;font-weight:600;color:var(--brand-green)}
.brand-dot{width:18px;height:18px;border-radius:50%;background:var(--brand-green)}
.lang-switch{right:134px;top:41px;font-size:13px;font-weight:600;color:var(--lang);letter-spacing:.3px}
.lang-switch span{margin:0 8px}
.lang-switch .active{color:var(--lang-active)}
.main-nav{right:134px;top:99px;display:flex;gap:32px;font-size:13px;color:#555}
.main-nav .active{color:var(--brand-green)}

/* hero */
.hero-photo{left:0;top:133px}
.hero-arrow{width:29px;height:29px;background:#222;top:359px}
.hero-arrow.prev{left:0}
.hero-arrow.next{right:0}
.hero-title{left:0;width:1200px;top:540px;text-align:center;font-size:32px;font-weight:700;line-height:39px;color:#333}

/* mission */
.section-title{left:0;width:1200px;text-align:center;font-weight:600;font-size:34px}
.mission-title{top:818px;color:var(--navy)}
.mission-lead{left:0;width:1200px;top:865px;text-align:center;font-size:21px;color:#111}
.mission-body{left:0;width:1200px;top:899px;text-align:center;font-size:13px;color:#333}
.product-note{left:0;width:1200px;top:930px;text-align:center;font-size:13px;color:#333}
.product-note strong{color:var(--teal);font-weight:600}

/* services */
.services-title{top:1186px;color:var(--teal);font-size:32px}
.service-card{top:1255px;width:298px;height:276px;border:2px solid var(--card-line);text-align:center;padding:0 16px}
.service-card svg{display:block;margin:28px auto 0}
.service-name{color:var(--teal);font-size:20px;font-weight:500;line-height:26px;margin-top:8px}
.service-name sup{font-size:12px}
.service-text{font-size:12px;line-height:19px;color:#444;margin-top:12px}

/* contact */
.contact-title{top:1723px;color:var(--navy)}
.field{height:34px;background:#fff;border:1px solid #d3d6d9;font-size:11px;color:#666;padding:0 15px;display:flex;align-items:center;justify-content:space-between}
.field .caret{width:0;height:0;border-left:5px solid transparent;border-right:5px solid transparent;border-top:6px solid #555}
.submit{left:562px;top:1886px;width:76px;height:35px;background:var(--ink);color:#fff;font-size:13px;font-weight:700;display:flex;align-items:center;justify-content:center}

/* footer */
.footer-links{left:133px;top:2085px;font-size:12px;color:var(--muted)}
.footer-links span{margin:0 9px}
.copyright{left:133px;top:2118px;font-size:12px;color:var(--muted)}
.social{left:982px;top:2106px;display:flex;gap:22px}
.social i{display:block;width:13px;height:13px;border-radius:50%;background:var(--muted)}
</style>
</head>
<body>

<svg class="abs page-bg" width="1200" height="2177" viewBox="0 0 1200 2177" aria-hidden="true">
  <rect width="1200" height="2177" fill="#f3f3f3"/>
  <rect y="133" width="1200" height="992" fill="#fff"/>
  <polygon points="0,1125 131,997 1200,1135 1200,1677 0,1611" fill="#e9ecee"/>
  <polygon points="795,1081 1098,1045 1200,1135" fill="#76c6b8"/>
  <polygon points="0,2058 1066,2003 1200,2053 1200,2177 0,2177" fill="#141a33"/>
</svg>

<header class="abs site-header">
  <div class="abs brand"><span class="brand-dot"></span>Ternly</div>
  <div class="abs lang-switch">GERMAN<span>|</span><span class="active" style="margin:0">ENGLISH</span><span>|</span>JAPANESE</div>
  <nav class="abs main-nav">
    <span class="active">Home</span><span>Mission</span><span>Services</span><span>Contact</span><span>Privacy</span><span>Terms &amp; Conditions</span>
  </nav>
</header>

<svg class="abs hero-photo" width="1200" height="620" viewBox="0 0 1200 620" role="img" aria-label="Photo of a woman at a desk working on a project management timeline on a desktop monitor, with a potted plant and pencils">
  <defs>
    <linearGradient id="heroTone" x1="0" y1="0" x2="1" y2="1">
      <stop offset="0" stop-color="#e6e1d8"/>
      <stop offset=".45" stop-color="#d9d8d4"/>
      <stop offset=".8" stop-color="#c9cfb9"/>
      <stop offset="1" stop-color="#e9e6df"/>
    </linearGradient>
  </defs>
  <polygon points="0,0 1200,0 1200,418 1073,619 0,484" fill="url(#heroTone)"/>
</svg>
<div class="abs hero-arrow prev" aria-hidden="true"><svg width="29" height="29" viewBox="0 0 29 29"><path d="M20 14.5H9M13 10l-4.5 4.5L13 19" stroke="#fff" stroke-width="2.2" fill="none"/></svg></div>
<div class="abs hero-arrow next" aria-hidden="true"><svg width="29" height="29" viewBox="0 0 29 29"><path d="M9 14.5h11M16 10l4.5 4.5L16 19" stroke="#fff" stroke-width="2.2" fill="none"/></svg></div>
<h1 class="abs hero-title">IT CONSULTING AND<br>SYSTEM DEVELOPMENT</h1>

<h2 class="abs section-title mission-title">Our Mission</h2>
<p class="abs mission-lead">Our mission is to achieve business goals with customers.</p>
<p class="abs mission-body">We work together to identify the goals for your company, guides your strategy and bring the technology answers which best fit to achieve the goals.</p>
<p class="abs product-note">With our workflow tool <strong>velmora</strong>, communication and tasks stay smooth, transparent and efficient at all levels.</p>

<h2 class="abs section-title services-title">What we do</h2>

<article class="abs service-card" style="left:133px">
  <svg width="72" height="66" viewBox="0 0 72 66" fill="none" stroke="#0e3d8a" stroke-width="2.4">
    <rect x="2" y="2" width="68" height="62"/><line x1="2" y1="11" x2="70" y2="11"/>
    <rect x="27" y="18" width="18" height="11"/><line x1="36" y1="29" x2="36" y2="37"/>
    <line x1="16" y1="37" x2="56" y2="37"/><line x1="16" y1="37" x2="16" y2="44"/><line x1="36" y1="37" x2="36" y2="44"/><line x1="56" y1="37" x2="56" y2="44"/>
    <rect x="9" y="44" width="14" height="10"/><rect x="29" y="44" width="14" height="10"/><rect x="49" y="44" width="14" height="10"/>
  </svg>
  <h3 class="service-name">Project Management<sup>(PM)</sup><br>Service</h3>
  <p class="service-text">We will provide end-to-end PM service with experienced PM. Our service is not only “managing” but “leading” to bring success to achieve the goal.</p>
</article>

<article class="abs service-card" style="left:451px">
  <svg width="72" height="66" viewBox="0 0 72 66" fill="none" stroke="#0e3d8a" stroke-width="2.4">
    <circle cx="36" cy="18" r="10"/><circle cx="36" cy="18" r="4"/>
    <path d="M36 2v5M36 29v4M20 18h5M47 18h5M25 7l3 3M44 26l3 3M47 7l-3 3"/>
    <rect x="4" y="30" width="64" height="28"/><line x1="30" y1="58" x2="42" y2="58"/><line x1="24" y1="64" x2="48" y2="64"/>
    <circle cx="16" cy="44" r="6"/><line x1="28" y1="40" x2="60" y2="40"/><line x1="28" y1="48" x2="52" y2="48"/>
  </svg>
  <h3 class="service-name">System Development &amp;<br>Implementation Service</h3>
  <p class="service-text">Our client list includes a wide variety of small to medium to major sized enterprises. We can offer from full-scratch based development to packaged system implementation.</p>
</article>

<article class="abs service-card" style="left:769px">
  <svg width="72" height="66" viewBox="0 0 72 66" fill="none" stroke="#0e3d8a" stroke-width="2.4">
    <path d="M22 4h46v30H56v10l-10-10H44"/>
    <path d="M4 18h40v30H20l-10 10V48H4z"/>
    <line x1="12" y1="28" x2="36" y2="28"/><line x1="12" y1="36" x2="32" y2="36"/>
  </svg>
  <h3 class="service-name">Consultation Service</h3>
  <p class="service-text" style="margin-top:38px">Consulting services to a wide range of fields such as creating business strategy, business process Kaizen, IT system consultation and change management.</p>
</article>

<h2 class="abs section-title contact-title">Contact Us</h2>
<div class="abs field" style="left:273px;top:1780px;width:207px">Name</div>
<div class="abs field" style="left:496px;top:1780px;width:208px">Email</div>
<div class="abs field" style="left:720px;top:1780px;width:207px">Service for<span class="caret"></span></div>
<div class="abs field" style="left:273px;top:1831px;width:654px">Messages</div>
<div class="abs submit">SUBMIT</div>

<nav class="abs footer-links">Home<span>|</span>Mission<span>|</span>Services<span>|</span>Contact<span>|</span>Privacy<span>|</span>Terms &amp; Conditions</nav>
<p class="abs copyright">Copyright © 2018 Ternly. All rights reserved.</p>
<div class="abs social" aria-label="Social links"><i></i><i></i><i></i></div>

</body>
</html>
```